Window Tinting

We are a window tinting company for automotive. Our main clientele has been the dealerships but now we are looking to expand to the general public. "Lumora" is actually short for LUMinosity (versus a measurement of time). We are hoping to make the "X" signature. Something easily noticed for later marketing. Right now since our name is kinda new, we'd rather the card scream "window tinting" versus our name being the main focus.. Window tint is a clean crisp aftermarket addition for vehicles and hopefully the business card can create that same attitude.

Industry/Entity Type

Automotive

Contact Information for Business Card

Lumora Tints Llc Dorin "Pike" Walsh
218 Kelby Rd. unit C
North Haven, Ct 06519 203.555.0172

```html
<!DOCTYPE html>
<html lang="en">
<head>
<meta charset="utf-8">
<title>Lumora Tints – Business Card</title>
<link rel="stylesheet" href="https://fonts.googleapis.com/css2?family=Lato:wght@300;400;700&display=swap">
<style>
  :root {
    --backdrop: #3a3330;
    --card-black: #141414;
    --card-edge: #0c0c0c;
    --accent-red: #e0282e;
    --text-white: #f2f2f2;
    --silver: #b9b9b9;
  }
  * { box-sizing: border-box; margin: 0; padding: 0; }
  html, body {
    width: 1200px;
    height: 844px;
    overflow: hidden;
    background: var(--backdrop);
    font-family: "Lato", sans-serif;
  }
  .stage {
    position: relative;
    width: 1200px;
    height: 844px;
  }
  .card {
    position: absolute;
    top: 279px;
    width: 500px;
    height: 286px;
    background: var(--card-black);
    border: 1px solid var(--card-edge);
    box-shadow: 0 12px 30px rgba(0,0,0,0.45);
  }
  .card--front { left: 70px; }
  .card--back { left: 630px; }

  /* Brand lockup */
  .brand {
    position: absolute;
    display: flex;
    align-items: center;
    gap: 10px;
    white-space: nowrap;
  }
  .brand__mark {
    flex: none;
    width: 22px;
    height: 22px;
    background: var(--accent-red);
  }
  .brand__name {
    font-weight: 300;
    font-size: 28px;
    letter-spacing: 0.5px;
    line-height: 1;
    color: var(--text-white);
  }
  .card--front .brand { left: 36px; top: 128px; }
  .card--back .brand { left: 50%; top: 50%; transform: translate(-50%, -50%); }
  .card--back .brand__name { font-size: 34px; color: var(--silver); }
  .card--back .brand__mark { width: 26px; height: 26px; background: var(--silver); }

  /* Contact column */
  .contact {
    position: absolute;
    left: 290px;
    top: 54px;
    color: var(--text-white);
    font-size: 13px;
    line-height: 1.4;
    white-space: nowrap;
  }
  .contact__name {
    color: var(--accent-red);
    font-size: 18px;
    font-weight: 400;
    line-height: 1.15;
  }
  .contact__role { margin-bottom: 14px; }
  .contact__address { margin-bottom: 14px; }
  .contact__label { color: var(--accent-red); display: inline-block; width: 18px; }
</style>
</head>
<body>
<main class="stage">
  <section class="card card--front" aria-label="Card front">
    <div class="brand">
      <span class="brand__name">Lumora Tints</span>
      <span class="brand__mark"></span>
    </div>
    <div class="contact">
      <p class="contact__name">Dorin Walsh</p>
      <p class="contact__role">Managing Director</p>
      <p class="contact__address">218 Kelby Rd. unit C<br>North Haven, Ct 06519</p>
      <p><span class="contact__label">T:</span> 203.555.0172</p>
      <p><span class="contact__label">E:</span> info@lumoratints.com</p>
      <p><span class="contact__label">W:</span> www.lumoratints.com</p>
    </div>
  </section>

  <section class="card card--back" aria-label="Card back">
    <div class="brand">
      <span class="brand__name">Lumora Tints</span>
      <span class="brand__mark"></span>
    </div>
  </section>
</main>
</body>
</html>
```